Testosterone clinic billboard

Design billboard for Male Testosterone therapy simple to the point but eye catching.
Contact info for the billboard - Vantorelix.com
Phone - 919-457-2186

Target Market(s)

Males with disposable income

Industry/Entity Type

medical

Requirements
Must have
• Testosterone Therapy, Erectile Dysfunction, Male Enhancement
Nice to have
• Simple, easy to read

```html
<!DOCTYPE html>
<html lang="en">
<head>
<meta charset="utf-8">
<title>Vantorelix – Male Testosterone Therapy Billboard</title>
<link href="https://fonts.googleapis.com/css2?family=Oswald:wght@700&family=Montserrat:wght@700;800&display=swap" rel="stylesheet">
<style>
  :root {
    --purple: #6a1d7a;
    --teal: #045f63;
    --white: #ffffff;
    --backdrop: #d9d9d9;
    --photo-warm: #c9b39c;
    --photo-cool: #c7c9cc;
    --photo-soft: #d8c7bb;
  }
  * { box-sizing: border-box; margin: 0; padding: 0; }
  html, body {
    width: 938px; height: 1200px; overflow: hidden;
    background: var(--backdrop);
  }
  .billboard {
    position: absolute; left: 29px; top: 380px;
    width: 880px; height: 440px;
    background: var(--white);
    border-bottom: 5px solid var(--teal);
    box-shadow: 0 10px 24px rgba(0,0,0,.35);
    overflow: hidden;
  }
  .top-band {
    position: absolute; left: 0; top: 0; width: 100%; height: 233px;
    background: var(--purple);
  }
  .headline {
    position: absolute; left: 0; right: 0; top: 26px;
    text-align: center;
    font-family: 'Oswald', sans-serif; font-weight: 700;
    font-size: 58px; line-height: 1; letter-spacing: 0.5px;
    color: var(--white);
  }
  .services {
    position: absolute; left: 61px; top: 98px;
    display: flex; gap: 17px;
  }
  .service { width: 241px; }
  .service-photo { height: 134px; }
  .photo-couple-outdoor { background: linear-gradient(135deg, #9fae7c, var(--photo-warm) 55%, #e9ddd0); }
  .photo-man-worried { background: linear-gradient(135deg, #3a4660, var(--photo-cool) 55%, #eeeeee); }
  .photo-couple-close { background: linear-gradient(135deg, #f2ece6, var(--photo-soft) 50%, #a57d66); }
  .service-label {
    height: 72px; padding: 12px 0 0 27px;
    font-family: 'Montserrat', sans-serif; font-weight: 800;
    font-size: 20px; line-height: 1.15; color: var(--white);
  }
  .label-purple { background: var(--purple); border-bottom: 2px solid var(--teal); }
  .label-teal { background: var(--teal); border-bottom: 2px solid var(--purple); }
  .brand-name {
    position: absolute; left: 60px; top: 332px;
    font-family: 'Montserrat', sans-serif; font-weight: 800;
    font-size: 54px; line-height: 1; color: var(--purple);
  }
  .contact {
    position: absolute; right: 62px; top: 322px;
    font-family: 'Montserrat', sans-serif; font-weight: 800;
  }
  .contact-row { display: flex; align-items: center; gap: 10px; }
  .contact-row svg { flex: none; }
  .phone { font-size: 40px; color: var(--teal); line-height: 1.1; }
  .web { font-size: 27px; color: var(--purple); margin-top: 4px; }
</style>
</head>
<body>
  <main class="billboard">
    <div class="top-band"></div>
    <h1 class="headline">MALE TESTOSTERONE THERAPY</h1>

    <section class="services">
      <article class="service">
        <div class="service-photo photo-couple-outdoor" role="img" aria-label="Photo of a smiling mature couple embracing outdoors"></div>
        <h2 class="service-label label-purple">TESTOSTERONE<br>THERAPY</h2>
      </article>
      <article class="service">
        <div class="service-photo photo-man-worried" role="img" aria-label="Photo of a worried man sitting on a bed with a woman in the background"></div>
        <h2 class="service-label label-teal">ERECTILE<br>DYSFUNCTION</h2>
      </article>
      <article class="service">
        <div class="service-photo photo-couple-close" role="img" aria-label="Photo of an affectionate young couple close together"></div>
        <h2 class="service-label label-purple">MALE<br>ENHANCEMENT</h2>
      </article>
    </section>

    <div class="brand-name">Vantorelix</div>

    <div class="contact">
      <div class="contact-row phone">
        <svg width="28" height="28" viewBox="0 0 28 28" aria-hidden="true">
          <circle cx="14" cy="14" r="14" fill="var(--teal)"/>
          <circle cx="14" cy="14" r="9.5" fill="none" stroke="#fff" stroke-width="1.6"/>
          <path d="M10.5 9.5c.6-.6 1.3-.5 1.7.1l.9 1.5c.3.5.2 1-.2 1.3l-.6.5c.5 1.2 1.5 2.2 2.7 2.8l.5-.6c.3-.4.9-.5 1.3-.2l1.5.9c.6.4.7 1.1.1 1.7-1 1-2.5 1.1-4.4-.2-1.5-1-2.7-2.3-3.6-3.8-1-1.7-.9-3 .1-4z" fill="#fff"/>
        </svg>
        <span>919-457-2186</span>
      </div>
      <div class="contact-row web">
        <svg width="28" height="28" viewBox="0 0 28 28" aria-hidden="true">
          <circle cx="14" cy="14" r="14" fill="var(--purple)"/>
          <g fill="none" stroke="#fff" stroke-width="1.4">
            <circle cx="14" cy="14" r="8"/>
            <ellipse cx="14" cy="14" rx="3.6" ry="8"/>
            <line x1="6" y1="14" x2="22" y2="14"/>
            <line x1="7.5" y1="10" x2="20.5" y2="10"/>
            <line x1="7.5" y1="18" x2="20.5" y2="18"/>
          </g>
        </svg>
        <span>Vantorelix.com</span>
      </div>
    </div>
  </main>
</body>
</html>
```